Larkfield Clinic Marketing Flyer

We are a new medical practice in the community and need a flyer to send to other medical offices to inform of our services. We just completed our logo with PixelGuild and would like to incorporate that plus our marketing content into the flyer. Our medical practice has 2 divisions: (1)Mental Health/Psychiatry and (2) Migraine and Neurospasticity Management. Please see website for content and provider photos at www.LarkfieldCare.example

Target Market(s)

Other Healthcare Professionals in the Community

Industry/Entity Type

Medical

Requirements
Must have
• Photos of all 5 healthcare providers, phone number, address, logo

```html
<!DOCTYPE html>
<html lang="en">
<head>
<meta charset="utf-8">
<title>Larkfield Clinic Flyer</title>
<link href="https://fonts.googleapis.com/css2?family=Cinzel:wght@500&family=Open+Sans:wght@400;600;700&family=Playfair+Display:wght@700;800&display=swap" rel="stylesheet">
<style>
:root{
  --teal:#16a196;
  --teal-dark:#0f7f77;
  --lime:#a4d94c;
  --lime-light:#c4e67a;
  --paper:#f8f7ee;
  --ink:#1c1c1c;
  --grey:#4a4a4a;
  --stage:#2b333d;
}
*{margin:0;padding:0;box-sizing:border-box}
html,body{width:1200px;height:2646px;overflow:hidden;background:var(--stage)}
.flyer{position:absolute;left:51px;top:614px;width:885px;height:1143px;background:var(--paper);overflow:hidden;transform:scale(1.24);transform-origin:top left;font-family:'Open Sans',sans-serif;color:var(--ink)}
.hero-photo{position:absolute;left:440px;top:-120px;width:680px;height:680px;border-radius:50%;background:radial-gradient(circle at 65% 45%,#e6b43a 0 14%,#5a4a3c 15% 24%,#d9d6cc 25% 55%,#b9b6a8 56%);border:7px solid var(--lime)}
.family-photo{position:absolute;left:522px;top:478px;width:270px;height:270px;border-radius:50%;background:radial-gradient(circle at 50% 55%,#c98a4a,#7a5a3a 60%,#4d3b2a);border:5px solid var(--paper)}
.brand{position:absolute;left:95px;top:95px;width:290px;text-align:center}
.brand-mark{width:90px;height:90px;border-radius:50%;background:var(--teal);margin:0 auto 20px}
.brand-name{font-family:'Cinzel',serif;font-weight:500;font-size:34px;color:var(--teal);letter-spacing:1px;line-height:1}
.tagline{position:absolute;left:95px;top:300px;font-family:'Playfair Display',serif;font-weight:800;font-size:44px;line-height:50px}
.tagline .t1{color:var(--teal)}
.tagline .t2{color:#fff}
.tagline .t3{color:var(--lime)}
.tag-band{position:absolute;left:0;top:360px;width:470px;height:48px;background:var(--teal-dark)}
.services{position:absolute;left:95px;top:462px;width:400px;font-weight:600;font-size:20px;line-height:24px}
.meet{position:absolute;left:95px;top:543px;font-family:'Playfair Display',serif;font-weight:800;font-size:38px;line-height:35px}
.intro{position:absolute;left:95px;top:632px;width:400px;font-size:15.5px;line-height:18px;color:var(--grey)}
.providers{position:absolute;left:80px;top:755px;display:flex;gap:27px}
.provider{width:116px;text-align:center}
.provider .portrait{width:116px;height:116px;border-radius:50%;background:radial-gradient(circle at 50% 40%,#cfa88a 0 30%,#55606a 31%)}
.provider .name{font-family:'Playfair Display',serif;font-weight:700;font-size:15px;line-height:16px;color:var(--teal);margin-top:6px;white-space:nowrap}
.features{position:absolute;left:100px;top:943px;display:flex}
.feature{display:flex;gap:12px;width:240px}
.feature svg{flex:none;margin-top:22px}
.feature h3{font-weight:600;font-size:16px;line-height:16px;color:var(--ink)}
.feature p{font-size:12px;line-height:12.5px;color:var(--grey);margin-top:6px;width:160px}
.footer{position:absolute;left:0;bottom:0;width:885px;height:52px}
.footer span{position:absolute;top:14px;color:#fff;font-size:14px;white-space:nowrap;display:flex;align-items:center;gap:6px}
.footer .phone{left:165px;top:10px;font-weight:700;font-size:22px}
.footer .web{left:410px}
.footer .addr{left:665px;top:8px;font-size:12px;line-height:13px}
</style>
</head>
<body>
<div class="flyer">
  <div class="hero-photo" role="img" aria-label="Photo of a smiling woman in a yellow top looking at her phone"></div>
  <div class="family-photo" role="img" aria-label="Photo of a happy family outdoors with pumpkins"></div>

  <div class="brand">
    <div class="brand-mark"></div>
    <div class="brand-name">Larkfield Clinic</div>
  </div>

  <div class="tag-band"></div>
  <div class="tagline">
    <div class="t1">Helping Bodies</div>
    <div class="t2">Helping Minds</div>
    <div class="t3">Helping You</div>
  </div>

  <p class="services">Mental Health and Psychiatry Services Migraine and Neurospasticity Intervention</p>
  <h2 class="meet">Meet Our Mental<br>Health Providers</h2>
  <p class="intro">Bringing comprehensive evaluation, medication management and psychotherapy to the full spectrum of mental health disorders including minor, moderate and major depression, bipolar disorder, ADD/ADHD, anxiety, schizophrenia, stress or grief reactions, and others.</p>

  <div class="providers">
    <div class="provider"><div class="portrait" role="img" aria-label="Portrait of Evan Marsh"></div><div class="name">Evan Marsh,<br>PMHNP - BC</div></div>
    <div class="provider"><div class="portrait" role="img" aria-label="Portrait of Dana Whitfield"></div><div class="name">Dana Whitfield,<br>PMHNP - BC</div></div>
    <div class="provider"><div class="portrait" role="img" aria-label="Portrait of Colin Brandt"></div><div class="name">Colin Brandt<br>PMHNP - BC</div></div>
    <div class="provider"><div class="portrait" role="img" aria-label="Portrait of Evan Marsh"></div><div class="name">Evan Marsh,<br>PMHNP - BC</div></div>
    <div class="provider"><div class="portrait" role="img" aria-label="Portrait of Dr. Alan Pryor"></div><div class="name">Dr. Alan<br>Pryor</div></div>
  </div>

  <div class="features">
    <div class="feature">
      <svg width="66" height="40" viewBox="0 0 66 40" fill="none" stroke="#222" stroke-width="2"><path d="M6 18c0-9 12-15 27-15s27 6 27 15-12 15-27 15c-4 0-8-.4-11-1.4L8 37l5-8C8 26 6 22 6 18z"/><circle cx="22" cy="18" r="2.5" fill="#222"/><circle cx="33" cy="18" r="2.5" fill="#222"/><circle cx="44" cy="18" r="2.5" fill="#222"/></svg>
      <div><h3>New Patient<br>Evaluation</h3><p>Consults provided for evaluation and management of patients with chronic migraines or neurospasticity challenges.</p></div>
    </div>
    <div class="feature">
      <svg width="46" height="44" viewBox="0 0 46 44" fill="none" stroke="#222" stroke-width="2"><rect x="2" y="2" width="28" height="38"/><path d="M8 10h16M8 16h16M8 22h10"/><path d="M36 8v30l4 4 4-4V8z"/></svg>
      <div><h3>Insurance<br>Pre-Authorization</h3><p>Botulinum toxin injections may be a recommended treatment option. If so, our office completes insurance pre-authorizations on your behalf.</p></div>
    </div>
    <div class="feature">
      <svg width="46" height="40" viewBox="0 0 46 40" fill="none" stroke="#222" stroke-width="2"><rect x="2" y="5" width="42" height="33"/><path d="M2 13h42M2 21h42M2 29h42M12 5v33M22 5v33M32 5v33M12 1v6M32 1v6"/></svg>
      <div><h3>Follow-Up<br>Appointments</h3><p>Timely appointments following insurance approval are available to quickly get you on the road to relief.</p></div>
    </div>
  </div>

  <div class="footer">
    <svg width="885" height="52" viewBox="0 0 885 52">
      <path d="M165 52 L185 20 Q195 4 215 4 H360 Q378 4 386 18 L405 52Z" fill="var(--teal)"/>
      <path d="M390 52 L410 18 Q418 4 438 4 H600 Q618 4 626 18 L645 52Z" fill="var(--lime)"/>
      <path d="M630 52 L650 18 Q658 4 678 4 H855 Q872 4 885 20 V52Z" fill="var(--teal)"/>
    </svg>
    <span class="phone"><svg width="16" height="16" viewBox="0 0 24 24" fill="#fff"><path d="M6.6 10.8a15 15 0 006.6 6.6l2.2-2.2c.3-.3.7-.4 1-.2 1.1.4 2.3.6 3.6.6.6 0 1 .4 1 1V20c0 .6-.4 1-1 1A17 17 0 013 4c0-.6.4-1 1-1h3.5c.6 0 1 .4 1 1 0 1.3.2 2.5.6 3.6.1.3 0 .7-.2 1z"/></svg>555-014-2270</span>
    <span class="web"><svg width="14" height="14" viewBox="0 0 24 24" fill="none" stroke="#fff" stroke-width="2"><circle cx="12" cy="12" r="10"/><path d="M2 12h20M12 2c3 3 3 17 0 20M12 2c-3 3-3 17 0 20"/></svg>www.LarkfieldCare.example</span>
    <span class="addr"><svg width="12" height="16" viewBox="0 0 24 32" fill="#fff"><path d="M12 0C5 0 0 5 0 12c0 9 12 20 12 20s12-11 12-20C24 5 19 0 12 0zm0 17a5 5 0 110-10 5 5 0 010 10z"/></svg><span style="position:static">120 Meadow Row, Suite B<br>Brookhaven, ID 83000</span></span>
  </div>
</div>
</body>
</html>
```